Minimalist, Flat(Matte) design for a Beef Jerky packaging company. No bullshit company looking for a

Need a packaging design for a new Beef Jerky product(in English). The name of the company is 'Vellorn' and thus the packaging should reflect the bullish, tough, and simple nature of the beef jerky product. The finished product should communicate simplicity, minimalism, yet toughness and strength.

The logo should be simple, with a minimal number of colors , and should be either all white/cream, or have some red as well. Main colors should be white, cream, tinted red, and matte black. I think 4 colors max would be best. The closest example to an existing package style would be Kessip Noir clove cigarettes( image attached).

It will be on a matte black standing pouch package. See image for package type. Package dimensions:

Dimension: Width x Gusset x Height
INCH : 5.125" (W) x 3.125" (G) x 8.125" (H)
MILLIMETER : 130mm (W) x 80mm (G) x 205mm (H)

I don't have anything totally specific so artistic liberty is encouraged, provided the colors are kept to a minimum and looks consistent with the simple nature of the brand and the matte black packaging.

Also attached an existing beef jerky package with a similar style to what we're looking for.

Industry/Entity Type

It Company

Colors
f59195
ffffff

Requirements
Must have
• Low contrast, flat and minimalist design.
Should not have
• A complicated design with many colors. Gawdy/flashy design. Bright colors. High contrast.

```html
<!DOCTYPE html>
<html lang="en">
<head>
<meta charset="utf-8">
<title>Vellorn Co. — Hand Crafted Beef Jerky, Peppered</title>
<link rel="stylesheet" href="https://fonts.googleapis.com/css2?family=Cinzel:wght@500&family=EB+Garamond:wght@500&display=swap">
<style>
  :root {
    --backdrop: #f1f1f1;
    --pouch-black: #1f1f1f;
    --pouch-edge: #2a2a2a;
    --seal-line: #383838;
    --cream: #e9dcb2;
  }
  html, body {
    margin: 0;
    padding: 0;
    width: 1200px;
    height: 1000px;
    overflow: hidden;
    background: var(--backdrop);
  }
  .canvas {
    position: relative;
    width: 1200px;
    height: 1000px;
  }
  .pouch {
    position: absolute;
    left: 345px;
    top: 90px;
    width: 525px;
    height: 760px;
    background: var(--pouch-black);
    border: 1px solid var(--pouch-edge);
    box-sizing: border-box;
  }
  .zip-seal {
    position: absolute;
    left: 30px;
    right: 30px;
    height: 2px;
    background: var(--seal-line);
  }
  .zip-seal.top { top: 82px; }
  .zip-seal.mid { top: 116px; }
  .zip-seal.low { top: 150px; }
  .label {
    position: absolute;
    left: 0;
    right: 0;
    text-align: center;
    color: var(--cream);
    margin: 0;
  }
  .brand-mark {
    top: 260px;
    font-family: "Cinzel", serif;
    font-weight: 500;
    font-size: 40px;
    letter-spacing: 1px;
    line-height: 1;
  }
  .brand-divider {
    position: absolute;
    left: 190px;
    top: 345px;
    width: 120px;
    height: 16px;
  }
  .product-name {
    top: 430px;
    font-family: "Cinzel", serif;
    font-weight: 500;
    font-size: 39px;
    line-height: 58px;
    letter-spacing: 1px;
  }
  .flavour {
    top: 575px;
    font-family: "Cinzel", serif;
    font-weight: 500;
    font-size: 41px;
    letter-spacing: 1px;
    line-height: 1;
  }
  .net-weight {
    top: 728px;
    font-family: "EB Garamond", serif;
    font-weight: 500;
    font-size: 16px;
    line-height: 1;
  }
</style>
</head>
<body>
  <main class="canvas">
    <section class="pouch">
      <div class="zip-seal top"></div>
      <div class="zip-seal mid"></div>
      <div class="zip-seal low"></div>

      <p class="label brand-mark">VELLORN CO.</p>

      <svg class="brand-divider" viewBox="0 0 120 16" aria-hidden="true">
        <line x1="0" y1="1" x2="120" y2="1" stroke="var(--cream)" stroke-width="2"/>
        <polygon points="48,2 72,2 60,14" fill="var(--cream)"/>
      </svg>

      <h1 class="label product-name">HAND CRAFTED<br>BEEF JERKY</h1>
      <p class="label flavour">PEPPERED</p>
      <p class="label net-weight">Net weight: 3 oz/100g</p>
    </section>
  </main>
</body>
</html>
```